Doctors clinic requires stationary designed

We require various types of stationary to be design based on the logo (attached). We require the following:
- Letterhead (A4 Portrait)
- Business Card (must include UV spot on rear)
- With compliments slip (DL Landscape)
- Appointments card (Folded A6)

We are a young clinical practice which boasts a modern and sophisticated approach to medicine so we require something which feels fresh and modern. Please include colours represented in the logo (contrasting teal and grey). We are calling for creative minds to put forth their ideas and we will be actively providing feedback on all designs.

thank you

```html
<!DOCTYPE html>
<html lang="en">
<head>
<meta charset="utf-8">
<title>Dr Clara Hensley – Letterhead</title>
<link rel="stylesheet" href="https://fonts.googleapis.com/css2?family=Exo+2:ital,wght@0,400;0,600;1,400&display=swap">
<style>
  :root {
    --backdrop: #b9dfcc;
    --paper: #f4f4f3;
    --teal: #1b7b70;
    --grey: #8fa09c;
    --ink: #3b3b3b;
    --sign-tone: #e3e6e5;
  }
  * { box-sizing: border-box; margin: 0; padding: 0; }
  html, body {
    width: 1200px;
    height: 1000px;
    overflow: hidden;
    background: var(--backdrop);
    font-family: "Exo 2", sans-serif;
    color: var(--ink);
  }
  .letterhead {
    position: absolute;
    left: 270px;
    top: 33px;
    width: 660px;
    height: 934px;
    background: var(--paper);
  }
  .brand {
    position: absolute;
    left: 34px;
    top: 80px;
    display: flex;
    align-items: center;
    gap: 14px;
  }
  .brand-dot {
    width: 62px;
    height: 62px;
    border: 2.5px solid var(--teal);
    border-radius: 50%;
  }
  .brand-name {
    font-size: 25px;
    font-weight: 600;
    color: var(--teal);
    line-height: 1.1;
  }
  .brand-role {
    font-size: 14px;
    font-weight: 600;
    color: var(--teal);
    line-height: 1.2;
  }
  .contact {
    position: absolute;
    left: 462px;
    top: 96px;
    list-style: none;
    font-size: 7.5px;
    line-height: 8.5px;
    color: #555;
  }
  .contact li { display: flex; align-items: center; gap: 4px; }
  .contact svg { width: 6px; height: 6px; fill: var(--teal); flex: none; }
  .letter {
    position: absolute;
    left: 123px;
    top: 240px;
    width: 432px;
  }
  .salutation {
    font-style: italic;
    font-size: 12.5px;
    margin-bottom: 22px;
  }
  .letter p.body {
    font-size: 10px;
    line-height: 15.2px;
    text-align: justify;
    margin-bottom: 21px;
  }
  .closing {
    position: absolute;
    right: 105px;
    top: 668px;
    font-style: italic;
    font-size: 12.5px;
  }
  .signature {
    position: absolute;
    left: 319px;
    top: 712px;
    width: 190px;
    height: 36px;
    background: var(--sign-tone);
    border-radius: 4px;
  }
</style>
</head>
<body>
  <main class="letterhead">
    <header class="brand">
      <div class="brand-dot"></div>
      <div>
        <div class="brand-name">Dr Clara Hensley</div>
        <div class="brand-role">Obstetrician and Gynaecologist</div>
      </div>
    </header>

    <ul class="contact">
      <li><svg viewBox="0 0 10 10"><path d="M5 0a3.5 3.5 0 0 0-3.5 3.5C1.5 6 5 10 5 10s3.5-4 3.5-6.5A3.5 3.5 0 0 0 5 0z"/></svg>18 Alder Lane, Westbrook,</li>
      <li><svg viewBox="0 0 10 10"></svg>Postcode, Country</li>
      <li><svg viewBox="0 0 10 10"><path d="M2 0h2l1 3-1.5 1a6 6 0 0 0 2.5 2.5L7 5l3 1v2a2 2 0 0 1-2 2A8 8 0 0 1 0 2a2 2 0 0 1 2-2z"/></svg>555-0142-87</li>
      <li><svg viewBox="0 0 10 10"><rect x="0" y="2" width="10" height="7" rx="1"/></svg>555-0142-88</li>
      <li><svg viewBox="0 0 10 10"><path d="M0 2h10v6H0zM0 2l5 4 5-4"/></svg>hello@hensleyclinic.com</li>
      <li><svg viewBox="0 0 10 10"><circle cx="5" cy="5" r="5"/></svg>www.hensleyclinic.com</li>
    </ul>

    <section class="letter">
      <p class="salutation">Dear Client,</p>
      <p class="body">Lorem ipsum dolor sit amet, consectetur adipiscing elit. Nulla sodales nisi vitae Lorem ipsum dolor sit amet, consectetur adipiscing elit. Suspendisse feugiat eros nisl, a facilisis risus eleifend sed. Aliquam mauris enim, fermentum eu lacinia sit amet, laoreet eu leo. Nullam eleifend nulla in libero tristique, ac vulputate odio tincidunt. Etiam non condimentum tortor. Integer suscipit neque nec odio porttitor cursus. Phasellus a sapien blandit, suscipit justo id, condimentum ante. Morbi tristique justo risus, id mattis dui molestie ut. Nullam volutpat ut quam commodo faucibus. Pellentesque urna est, interdum in elit quis, pharetra elementum orci. Nam pharetra velit molestie justo placerat scelerisque.</p>
      <p class="body">Sed est tellus, rutrum in nisl a, consequat sollicitudin elit. Aliquam vitae vestibulum felis. Morbi iaculis nunc volutpat diam ullamcorper vestibulum. Nulla facilisi. Aenean accumsan gravida orci, vitae consectetur justo aliquet et. Curabitur vehicula tempus dolor, a gravida metus vestibulum sit amet. Integer non erat elementum, malesuada metus vel, fermentum lectus. Etiam sit amet nisl ac augue semper ultrices.</p>
      <p class="body">Nulla tincidunt molestie libero vel pretium. Donec condimentum nulla sit amet risus semper imperdiet. Duis congue eros nec diam blandit, et pellentesque sapien auctor. Curabitur iaculis enim lectus, in imperdiet mauris mattis eget. Etiam ac ornare metus. Mauris risus leo, egestas at dolor a, ultrices adipiscing est. Nunc faucibus scelerisque mollis. Pellentesque aliquet mauris tellus, id dignissim risus viverra et. Mauris venenatis lobortis eros. Nam id diam in ligula malesuada feugiat. Cras turpis felis, aliquet id mauris elementum, feugiat ultricies nisl.</p>
    </section>

    <p class="closing">Best regards.</p>
    <div class="signature" role="img" aria-label="Handwritten signature of Dr Clara Hensley"></div>
  </main>
</body>
</html>
```